Business card and e-mail signature template.

I need a business card- and e-mail signature template for a project (signature will be used with gmail). The logo is attached.

There the logo has a focus on the “Lumora” part of the name. The URL for the project is www.lumorafest.com.
The full name of the project is The Lumora Expo. The project will be publicly known as “Lumora” or “Lumora2020”. In all documents we will present the project as Lumora2020.

The logo can contain design elements and the design should be modern and appealing to both young people and traditional companies.

This competition is part of a bigger delivery. The winner will therefore be a strong candidate for the brand guide og maybe website.

```html
<!DOCTYPE html>
<html lang="en">
<head>
<meta charset="UTF-8">
<title>Lumora2020 Business Card</title>
<link href="https://fonts.googleapis.com/css2?family=Lato:wght@400;700&family=Montserrat:wght@600&display=swap" rel="stylesheet">
<style>
  :root {
    --stage: #4a4a4c;
    --paper: #ffffff;
    --ink: #8a8a8a;
    --ink-dark: #3b3b3b;
    --orange: #f2891f;
    --magenta: #e5245e;
    --green: #1e5a30;
    --green-light: #2f7a45;
  }
  * { margin: 0; padding: 0; box-sizing: border-box; }
  html, body { width: 1200px; height: 900px; overflow: hidden; }
  body {
    background: var(--stage);
    font-family: "Lato", Arial, sans-serif;
    position: relative;
  }
  .card {
    position: absolute;
    width: 600px;
    height: 343px;
    overflow: hidden;
  }
  .card--front { left: 80px; top: 100px; background: var(--paper); }
  .card--back { left: 520px; top: 470px; background: var(--green); }

  .card__swoosh { position: absolute; inset: 0; }

  .brand {
    position: absolute;
    display: flex;
    align-items: center;
    gap: 14px;
    font-family: "Montserrat", Arial, sans-serif;
    font-weight: 600;
    letter-spacing: 1px;
    white-space: nowrap;
  }
  .brand__dot { flex: none; border-radius: 50%; background: var(--magenta); }
  .brand__name { display: flex; flex-direction: column; line-height: 1.05; }
  .card--front .brand { left: 72px; top: 118px; font-size: 28px; color: var(--ink-dark); }
  .card--front .brand__dot { width: 22px; height: 22px; }
  .card--back .brand { left: 170px; top: 112px; font-size: 44px; color: var(--paper); }
  .card--back .brand__dot { width: 30px; height: 30px; }

  .contact {
    position: absolute;
    left: 300px;
    top: 44px;
    padding-left: 18px;
    border-left: 2px solid var(--orange);
    color: var(--ink);
    font-size: 13px;
    line-height: 1.4;
  }
  .contact__name { color: var(--orange); font-size: 22px; font-weight: 700; margin-bottom: 8px; }
  .contact__address { margin-bottom: 10px; }
  .contact__row { display: flex; align-items: center; gap: 8px; margin-bottom: 3px; }
  .contact__icon { width: 14px; height: 14px; flex: none; }

  .social {
    position: absolute;
    left: 450px;
    top: 236px;
    display: flex;
    align-items: center;
    gap: 8px;
    color: var(--paper);
    font-size: 13px;
    font-weight: 700;
    white-space: nowrap;
  }
  .social__dot { width: 12px; height: 12px; border-radius: 50%; background: var(--paper); }

  .pattern { position: absolute; inset: 0; background: radial-gradient(circle at 50% 50%, var(--green-light), var(--green) 75%); }
</style>
</head>
<body>

<section class="card card--front">
  <svg class="card__swoosh" viewBox="0 0 600 343" width="600" height="343" aria-hidden="true">
    <path d="M0 325 C200 345 400 200 600 160 L600 343 L0 343 Z" fill="var(--orange)"/>
    <path d="M0 300 C180 320 330 260 420 225 C330 275 180 330 0 316 Z" fill="var(--magenta)"/>
  </svg>

  <div class="brand"><span class="brand__dot"></span><span class="brand__name"><span>LUMORA</span><span>2020</span></span></div>

  <div class="contact">
    <p class="contact__name">Noa Brenner</p>
    <p class="contact__address">48 Harbor Lane 3rd Floor<br>Portland city -2210</p>
    <p class="contact__row">
      <svg class="contact__icon" viewBox="0 0 14 14"><circle cx="7" cy="7" r="7" fill="var(--orange)"/><path d="M4.5 3.5 L6 3.5 L6.6 5.3 L5.7 6 C6.1 7 7 7.9 8 8.3 L8.7 7.4 L10.5 8 L10.5 9.5 C7 9.8 4.2 7 4.5 3.5 Z" fill="#fff"/></svg>
      555.204.71836
    </p>
    <p class="contact__row">
      <svg class="contact__icon" viewBox="0 0 14 14"><circle cx="7" cy="7" r="7" fill="var(--orange)"/><rect x="3.5" y="4.5" width="7" height="5" fill="#fff"/><path d="M3.5 4.5 L7 7.3 L10.5 4.5" stroke="var(--orange)" stroke-width="0.8" fill="none"/></svg>
      noa.brenner@mailbox.com
    </p>
    <p class="contact__row">
      <svg class="contact__icon" viewBox="0 0 14 14"><circle cx="7" cy="7" r="7" fill="var(--orange)"/><circle cx="7" cy="7" r="3.6" fill="none" stroke="#fff" stroke-width="0.9"/><path d="M3.4 7 H10.6 M7 3.4 V10.6" stroke="#fff" stroke-width="0.9"/></svg>
      www.lumorafest.com
    </p>
  </div>

  <p class="social"><span class="social__dot"></span><span>/lumora2020</span></p>
</section>

<section class="card card--back">
  <div class="pattern" role="img" aria-label="Repeating pattern of small connected dots and lines in soft green"></div>
  <div class="brand"><span class="brand__dot"></span><span class="brand__name"><span>LUMORA</span><span>2020</span></span></div>
</section>

</body>
</html>
```